Business Card Design Project

New business card design front and back for IT company that does network support and web design.
Calloway IT
Derek Calloway
Managing Director
PO Box 582 Tarrowby VIC 3267
derek@callowayit.example
www.callowayit.example

Industry/Entity Type

Business

```html
<!DOCTYPE html>
<html lang="en">
<head>
<meta charset="utf-8">
<title>Calloway IT — Business Card</title>
<link href="https://fonts.googleapis.com/css2?family=Lato:wght@300;400;700&display=swap" rel="stylesheet">
<style>
  :root {
    --page-bg: #eceef1;
    --card-navy: #0d2a58;
    --card-navy-deep: #0a2249;
    --card-navy-soft: #163468;
    --text-white: #ffffff;
    --text-muted: #d9e2f0;
    --accent-cyan: #2aa9e0;
  }
  * { box-sizing: border-box; margin: 0; padding: 0; }
  html, body {
    width: 1200px;
    height: 1000px;
    overflow: hidden;
    background: var(--page-bg);
    font-family: "Lato", sans-serif;
  }
  .canvas {
    position: relative;
    width: 1200px;
    height: 1000px;
  }
  .card {
    position: absolute;
    top: 350px;
    width: 535px;
    height: 300px;
    color: var(--text-white);
    box-shadow: 0 6px 14px rgba(0, 0, 0, 0.28);
    overflow: hidden;
  }
  .card--back { left: 47px; }
  .card--front { left: 618px; }
  .card__pattern {
    position: absolute;
    inset: 0;
    background: radial-gradient(ellipse at 50% 45%, var(--card-navy-soft) 0%, var(--card-navy) 55%, var(--card-navy-deep) 100%);
  }
  .identity {
    position: absolute;
    top: 20px;
    right: 22px;
    text-align: right;
  }
  .identity__name {
    font-size: 24px;
    font-weight: 400;
    line-height: 1.1;
  }
  .identity__role {
    font-size: 16px;
    font-weight: 300;
    color: var(--text-muted);
    margin-right: 22px;
  }
  .contact-list {
    position: absolute;
    left: 24px;
    top: 193px;
    list-style: none;
  }
  .contact-list__item {
    display: flex;
    align-items: center;
    height: 22px;
    font-size: 16px;
    font-weight: 400;
  }
  .contact-list__icon {
    width: 16px;
    height: 16px;
    margin-right: 10px;
    flex: none;
  }
  .brand {
    position: absolute;
    left: 0;
    right: 0;
    top: 110px;
    text-align: center;
  }
  .brand__name {
    font-size: 29px;
    font-weight: 700;
    letter-spacing: 0.5px;
    line-height: 1.2;
  }
  .brand__tagline {
    margin-top: 8px;
    font-size: 22px;
    font-weight: 400;
    color: var(--accent-cyan);
  }
</style>
</head>
<body>
<main class="canvas">

  <section class="card card--back" aria-label="Card back with contact details">
    <div class="card__pattern" role="img" aria-label="Subtle tonal navy circuit-trace pattern"></div>
    <div class="identity">
      <p class="identity__name">Derek Calloway</p>
      <p class="identity__role">Managing Director</p>
    </div>
    <ul class="contact-list">
      <li class="contact-list__item">
        <svg class="contact-list__icon" viewBox="0 0 16 16" aria-hidden="true">
          <circle cx="8" cy="8" r="7.3" fill="none" stroke="#fff" stroke-width="1.2"/>
          <path d="M5.2 4.3l1.4-.4.9 2-1 .7c.4 1 1.2 1.8 2.2 2.2l.7-1 2 .9-.4 1.4c-3 .4-6.2-2.8-5.8-5.8z" fill="#fff"/>
        </svg>
        0400 555 812
      </li>
      <li class="contact-list__item">
        <svg class="contact-list__icon" viewBox="0 0 16 16" aria-hidden="true">
          <circle cx="8" cy="8" r="7.3" fill="#fff"/>
          <text x="8" y="11.3" text-anchor="middle" font-family="Lato, sans-serif" font-size="10" font-weight="700" fill="#0d2a58">@</text>
        </svg>
        derek@callowayit.example
      </li>
      <li class="contact-list__item">
        <svg class="contact-list__icon" viewBox="0 0 16 16" aria-hidden="true">
          <circle cx="8" cy="8" r="7.3" fill="#fff"/>
          <g fill="none" stroke="#0d2a58" stroke-width="0.9">
            <circle cx="8" cy="8" r="4.6"/>
            <ellipse cx="8" cy="8" rx="2" ry="4.6"/>
            <path d="M3.4 8h9.2M4 5.8h8M4 10.2h8"/>
          </g>
        </svg>
        www.callowayit.example
      </li>
      <li class="contact-list__item">
        <svg class="contact-list__icon" viewBox="0 0 16 16" aria-hidden="true">
          <circle cx="8" cy="8" r="7.3" fill="#fff"/>
          <rect x="4" y="5.2" width="8" height="5.6" fill="#0d2a58"/>
          <path d="M4 5.4l4 3 4-3" fill="none" stroke="#fff" stroke-width="0.9"/>
        </svg>
        PO Box 582 Tarrowby VIC 3267
      </li>
    </ul>
  </section>

  <section class="card card--front" aria-label="Card front with company name">
    <div class="card__pattern" role="img" aria-label="Subtle tonal navy circuit-trace pattern"></div>
    <div class="brand">
      <h1 class="brand__name">CALLOWAY IT</h1>
      <p class="brand__tagline">IT Solutions For Your Business</p>
    </div>
  </section>

</main>
</body>
</html>
```